Anzeigengestaltung für Darstellung der Zentralaussagen einer PR-Agentur
Zielgruppe
Wir suchen ein hochwertiges und anspechendes Design für eine halbseitige (DIN A5) Werbeanzeige, um Insolvenzverwalter auf unsere PR-Arbeit für ihre eignenen Insolvenzfälle aufmerksam zu machen. Idealerweise übernimmt der Insolvenzverwalter also die rechtlichen Aufgaben innerhalb der Insolvenz und wir die kommunikativen, also die Öffentlichkeitsarbeit und interne Kommunikation. Meist schätzen die Anwälte hierbei dann unser breites Netzwerk (zu Journalisten etc.), unser Kommunikationsgefühl und, dass wir zudem rechtliches Verständnis mitbringen.
Unsere Zielgruppe sind somit Anwälte, die im Insolvenzrecht tätig sind, also als Insolvenzverwalter arbeite, sowie Unternehmen, denen eine Insolvenz droht oder sich in einer Insolvenz befinden.
Wir sind eine PR-Agenur, spezialisiert auf das juristische Umfeld. Wir beraten Unternehmen und Anwaltskanzleien, wie sie in Rechtsstreitigkeiten mit der Öffentlihkeit umgehen. Spezialisiert sind wir auf die Insolvenzkommunikation. Hier beraten wir die Insolvenzverwaltung und das von der Insolvenz betroffene Unternehmen in der internen und externen Kommunikation. Hierbei bringen wir als Unternehmen mit unseren Mitarbeitern Fachkenntnisse aus PR, sowie juristische Expertise mit, denn alle unsere Berater haben einen juristischen Abschluss. In einer juristischen Ausnahmesituation wie einer Insolvenz ist es für uns daher leicht, den Sachverhalt zu erfassen. Das hebt uns von anderen PR-Agenturen ab. Wir kümmern uns um alle kommunikativen Fragen, die innerhalb des Unternehmens während der Insolvenz auftreten und um Medienanfragen rund um die Insolvenz von außerhalb (klassische Presseanfragen). Verschwiegenheit und Diskretion gegenüber unserem Mandanten steht für uns dabei stets mit an oberster Stelle.
Aufgabenstellung
Wir möchten die Anzeige möglichst klassisch und seriös halten. Trotzdem sollte sie ins Auge fallen und herausstechen. Visuell sollte sie ansprechend sein und mit symbolhaften Bildern unterstrichen, da wir selbst als Berater nicht in der Anzeige abgebildet sein wollen. Textlich sollte es einen nicht erschlagen. Unsere Hauptdienstleistungen und Zentralaussagen sollten aber drin sein (juristische und kommunikative Expertise, interne und externe Insolvenzkommunikation, kein Ein-Mann-Betrieb, gut vernetzt)

```html
<!DOCTYPE html>
<html lang="de">
<head>
<meta charset="utf-8">
<title>LEXTON Rechtskommunikation – Anzeige</title>
<link rel="stylesheet" href="https://fonts.googleapis.com/css2?family=Cinzel:wght@400&family=Roboto:wght@300;400&display=swap">
<style>
  :root {
    --backdrop: #e0e0e0;
    --ink-black: #030303;
    --gold: #a3861a;
    --text-dark: #222222;
    --logo-grey: #3a3a3a;
    --paper: #ffffff;
  }
  * { margin: 0; padding: 0; box-sizing: border-box; }
  html, body {
    width: 1200px; height: 1200px; overflow: hidden;
    background: var(--backdrop);
  }
  .ad {
    position: absolute; left: 257px; top: 101px;
    width: 686px; height: 969px;
    background: var(--paper);
    overflow: hidden;
  }
  .hero {
    position: absolute; left: 0; top: 0; width: 100%; height: 556px;
    background: var(--ink-black);
  }
  .hero-photo {
    position: absolute; inset: 0;
    background:
      radial-gradient(ellipse 32% 22% at 27% 64%, rgba(190,190,190,0.55) 0%, rgba(120,120,120,0.2) 55%, rgba(0,0,0,0) 100%),
      radial-gradient(ellipse 30% 16% at 72% 70%, rgba(70,70,70,0.9) 0%, rgba(40,40,40,0.4) 60%, rgba(0,0,0,0) 100%),
      radial-gradient(ellipse 80% 28% at 55% 40%, #2e2e2e 0%, rgba(15,15,15,0) 70%),
      linear-gradient(180deg, #030303 0%, #080808 40%, #1e1e1e 62%, #4a4a4a 80%, #8a8a8a 88%, #3c3c3c 100%);
  }
  .hero-tint {
    position: absolute; left: 0; bottom: 0; width: 100%; height: 16px;
    background: linear-gradient(180deg, rgba(163,134,26,0.35), rgba(163,134,26,0.75));
  }
  .headline {
    position: absolute; left: 41px; top: 62px;
    font-family: "Cinzel", serif; font-weight: 400;
    color: #ffffff; font-size: 55px; line-height: 64px;
    letter-spacing: 0.5px;
  }
  .band-top {
    position: absolute; left: 0; top: 556px; width: 100%; height: 16px;
    background: var(--gold);
  }
  .body-copy {
    position: absolute; left: 41px; top: 597px; width: 604px;
    display: flex; justify-content: space-between;
    font-family: "Roboto", sans-serif; font-weight: 300;
    font-size: 11px; line-height: 16.2px; color: var(--text-dark);
  }
  .body-column { width: 295px; text-align: justify; text-align-last: justify; }
  .body-column:last-child { text-align-last: left; }
  .brand {
    position: absolute; left: 0; width: 100%; top: 756px;
    text-align: center;
    font-family: "Cinzel", serif; font-weight: 400;
    font-size: 46px; letter-spacing: 3px; color: var(--logo-grey);
    line-height: 1;
  }
  .claim {
    position: absolute; left: 0; width: 100%; top: 829px;
    text-align: center;
    font-family: "Roboto", sans-serif; font-weight: 400;
    font-size: 11.5px; line-height: 14.5px; color: var(--gold);
  }
  .contact {
    position: absolute; left: 0; width: 100%; top: 887px;
    display: flex; justify-content: center; gap: 12px;
    font-family: "Roboto", sans-serif; font-weight: 300; font-style: normal;
    font-size: 8.6px; line-height: 11px; color: var(--text-dark);
  }
  .contact-address { text-align: right; width: 200px; }
  .contact-lines { text-align: left; width: 200px; }
  .band-bottom {
    position: absolute; left: 0; bottom: 0; width: 100%; height: 27px;
    background: var(--gold);
  }
</style>
</head>
<body>
  <article class="ad">
    <section class="hero">
      <div class="hero-photo" role="img" aria-label="Schwarz-weißes Foto: weißer Springer steht neben einem umgefallenen schwarzen König auf einem Schachbrett"></div>
      <div class="hero-tint"></div>
      <h1 class="headline">Auch Niederlagen<br>brauchen den<br>Richtigen O-Ton</h1>
    </section>
    <div class="band-top"></div>

    <div class="body-copy">
      <p class="body-column">Nimust, anturem aborum suntem eosam, omnitia di ulpa&shy;rum quatium et eatem harias de quatur sume velestem il magnis maio dempedi cidellab iur, sin eatiosaerum ere po&shy;reptas exceriones eiures delit aut mo venihic tem resequate sunt ut omniet hillendus am, corectio dem ent volliquam a</p>
      <p class="body-column">sum rem nis cuptureperum idus eum velenduntio veniminti reptatem verferspe voloreribus id quam il maximol uptata dolupta turiam unt faces autem il iunt optaepudis issitatur sinum digniss imusaec epudandi cusdam quatemped quo con porunt rehent velenem alitatqui re nam exce.</p>
    </div>

    <div class="brand">LEXTON</div>

    <p class="claim">Wir kommunizieren für unsere Mandanten<br>Rechts- und Krisenthemen auf höchstem Niveau</p>

    <address class="contact">
      <div class="contact-address">LEXTON<br>Rechtskommunikation GmbH<br>Lindenallee 12<br>10115 Berlin</div>
      <div class="contact-lines">Tel.: +49 30 12 34 5670<br>Fax: +49 30 12 34 5671<br>post@lexton.media<br>lexton-rechtskommunikation.de</div>
    </address>

    <div class="band-bottom"></div>
  </article>
</body>
</html>
```